Business Card Design Project

We are a consulting company which works with tourism operators and attractions, wineries, heritage sites, National and conservation parks etc to help them identify their 'Point of Difference' and then deliver an exceptional tourism visitor experience.
We specialise in: Operator training, Site interpretation, Product and experience development, Planning and analysis.
We have a tag line of "Telling your story - really well."
The company name is MornVoice and the logo is this word with the 'Morn' in black and the 'Voice' in orange - but this can be changed. The 'a' is a speech bubble. A lot of what we do involves talking!
The design should communicate that we can make a big difference to the range and quality of experiences that visitors get at your site.
Updates

I put the wrong telephone number in my brief. My apologies.

It should be +61 0487 555 913

Target Market(s)

tourism busineses, wineries and cellar doors, heritage sites, environment managers, Government agencies & private companies

Industry/Entity Type

Tourism

Requirements
Must have
• Name: Ruth Pellow
Title: Emeritus Professor
Qualifications: BSc(Hons), PhD
Role: Director
Address: PO Box 317, Marlow Bay, South Reach 5871
Phone: (+61) 0487 555 913
Email: ruth@mornvoice-example.com.au
www.mornvoice-example.com.au
ABN 514 072 389 16

Operator Training, Site Interpretation, Product and Experience Development, Planning and Analysis.
Nice to have
• Awards:
Winner 2011 Coastline Visitor Honours – Kestrel College - Tourism Education and Training
Winner 2009 Coastline Visitor Honours - Outstanding Contribution by an Individual
Winner 2009 Gulfside Citizen Medal - Tourism Award
Should not have
• No 'shadows' to company name/logo please.
No black reverse side of card

```html
<!DOCTYPE html>
<html lang="en">
<head>
<meta charset="utf-8">
<title>MornVoice Consulting – Business Card</title>
<link rel="stylesheet" href="https://fonts.googleapis.com/css2?family=Arimo:ital,wght@0,400;0,700;1,400&display=swap">
<style>
  :root {
    --bg: #ebebeb;
    --card: #f4f4f4;
    --ink: #111111;
    --grey: #8a8a8a;
    --orange: #d0561f;
  }
  * { margin: 0; padding: 0; box-sizing: border-box; }
  html, body { width: 1200px; height: 800px; overflow: hidden; }
  body {
    background: var(--bg);
    font-family: "Arimo", Arial, sans-serif;
    color: var(--ink);
    position: relative;
  }
  .card {
    position: absolute;
    top: 250px;
    width: 520px;
    height: 300px;
    box-shadow: 0 2px 10px rgba(0,0,0,0.12);
  }
  .card--front { left: 50px; background: var(--card); }
  .card--back { left: 630px; background: var(--orange); }

  /* front */
  .brand { position: absolute; left: 40px; top: 42px; }
  .brand__name { font-size: 44px; font-weight: 700; letter-spacing: -1.5px; line-height: 1; color: var(--ink); }
  .brand__sub { font-size: 10px; letter-spacing: 3px; color: var(--grey); margin-top: 4px; padding-left: 74px; }

  .person { position: absolute; left: 70px; top: 150px; }
  .person__marker { position: absolute; left: -22px; top: 3px; width: 0; height: 0;
    border-left: 12px solid var(--orange); border-top: 7px solid transparent; border-bottom: 7px solid transparent; }
  .person__name { font-size: 17px; font-weight: 700; }
  .person__quals { font-size: 11px; font-weight: 400; }
  .person__role { font-size: 11px; font-weight: 700; margin-top: 1px; }
  .person__address { font-size: 11px; line-height: 1.35; margin-top: 16px; }

  .divider { position: absolute; left: 290px; top: 120px; }

  .contact { position: absolute; right: 26px; top: 44px; font-size: 11px; line-height: 1.45; text-align: right; }
  .contact__row { display: flex; justify-content: flex-end; align-items: center; gap: 6px; }
  .contact__icon { width: 10px; height: 10px; background: var(--orange); display: inline-block; }
  .contact__row--plain { padding-right: 16px; }

  .tagline { position: absolute; right: 60px; top: 222px; font-size: 11px; color: var(--grey); }

  /* back */
  .bubble-shape { position: absolute; inset: 0; }
  .awards { position: absolute; left: 150px; top: 55px; width: 320px; text-align: center; font-size: 10.5px; line-height: 1.25; }
  .awards__title { font-size: 12px; font-weight: 700; margin-bottom: 10px; }
  .awards__item { margin-bottom: 9px; }
</style>
</head>
<body>

<section class="card card--front" aria-label="Business card front">
  <div class="brand">
    <div class="brand__name">MornVoice</div>
    <div class="brand__sub">CONSULTING</div>
  </div>

  <div class="person">
    <span class="person__marker"></span>
    <div class="person__name">Ruth Pellow, <span class="person__quals">BSc (Hons), PhD</span></div>
    <div class="person__role">Director</div>
    <div class="person__address">PO Box 317, Marlow Bay<br>South Reach 5871</div>
  </div>

  <svg class="divider" width="60" height="60" viewBox="0 0 60 60" aria-hidden="true">
    <line x1="0" y1="0" x2="50" y2="50" stroke="#d0561f" stroke-width="0.8"/>
  </svg>

  <div class="contact">
    <div class="contact__row">ABN 514 072 389 16 <span class="contact__icon"></span></div>
    <div class="contact__row">(+61) 0487 555 913 <span class="contact__icon"></span></div>
    <div class="contact__row">ruth@mornvoice-example.com.au <span class="contact__icon"></span></div>
    <div class="contact__row contact__row--plain">www.mornvoice-example.com.au</div>
  </div>

  <div class="tagline">"Telling your story - really well."</div>
</section>

<section class="card card--back" aria-label="Business card back">
  <svg class="bubble-shape" width="520" height="300" viewBox="0 0 520 300" aria-hidden="true">
    <path d="M180 40 H440 Q480 40 480 80 V170 Q480 205 445 205 H440 L430 265 L405 205 H180 Q140 205 140 170 V80 Q140 40 180 40 Z" fill="#f4f4f4"/>
  </svg>
  <div class="awards">
    <div class="awards__title">Awards:</div>
    <div class="awards__item">Winner 2011 Coastline Visitor Honours – Kestrel College<br>- Tourism Education and Training</div>
    <div class="awards__item">Winner 2009 Coastline Visitor Honours - Outstanding<br>Contribution by an Individual</div>
    <div class="awards__item">Winner 2009 Gulfside Citizen Medal<br>- Tourism Award</div>
  </div>
</section>

</body>
</html>
```